Specialist aerospace company requires Powerpoint template

We are a company who delivers specialist engineering and testing services. We would like an updated Powerpoint template - specifically one that will be suitable to use in the production of training materials.
We would therefore like the following included:
-Our logo
-A copyright notice
-The course name (e.g. High Voltage Basics)
-The lesson name (e.g. Safe Clearances)
We wish to convey a professional image.

```html
<!DOCTYPE html>
<html lang="en">
<head>
<meta charset="utf-8">
<title>High Voltage Basics – Safe Clearances</title>
<link rel="stylesheet" href="https://fonts.googleapis.com/css2?family=Archivo:ital,wght@0,600;1,700;1,800&display=swap">
<style>
  :root {
    --brand-blue: #41729b;
    --ink: #454c55;
    --band: #f3f3f3;
    --page: #ffffff;
  }
  html, body {
    margin: 0;
    padding: 0;
    overflow: hidden;
    background: var(--page);
  }
  .slide {
    position: relative;
    width: 1200px;
    height: 848px;
    overflow: hidden;
    background: var(--page);
    font-family: "Archivo", Arial, sans-serif;
  }
  .brand {
    position: absolute;
    left: 89px;
    top: 80px;
    height: 50px;
    display: flex;
    align-items: center;
    gap: 20px;
  }
  .brand-mark {
    width: 48px;
    height: 48px;
    background: var(--brand-blue);
  }
  .brand-name {
    font-weight: 600;
    font-style: normal;
    font-size: 44px;
    letter-spacing: 0.5px;
    line-height: 1;
    color: var(--ink);
  }
  .content-band {
    position: absolute;
    left: 0;
    top: 197px;
    width: 1200px;
    height: 481px;
    background: var(--band);
  }
  .course-title {
    position: absolute;
    left: 550px;
    top: 76px;
    margin: 0;
    font-weight: 800;
    font-style: italic;
    font-size: 41px;
    line-height: 1.2;
    color: var(--brand-blue);
  }
  .lesson-title {
    position: absolute;
    left: 550px;
    top: 226px;
    margin: 0;
    font-weight: 700;
    font-style: italic;
    font-size: 30px;
    line-height: 1.2;
    color: var(--brand-blue);
  }
  .copyright {
    position: absolute;
    left: 550px;
    top: 789px;
    margin: 0;
    font-weight: 700;
    font-style: italic;
    font-size: 14px;
    color: var(--ink);
  }
</style>
</head>
<body>
  <main class="slide">
    <div class="content-band"></div>
    <div class="brand">
      <span class="brand-mark"></span>
      <span class="brand-name">voltaxisHV</span>
    </div>
    <h1 class="course-title">high voltage basics</h1>
    <h2 class="lesson-title">safe clearances</h2>
    <p class="copyright">A copyright notice</p>
  </main>
</body>
</html>
```